Business Card Design

Buy and sell properties
Buy and rehab properties
Buy properties for cash
That is what I do but do need a logo
looking for some type of logo or design on it
Just started business
Back of card should say something like BUY HOUSES CASH
Overview: it is a new company. Basically I buy properties wholesale and fix them up and sell them or sell them to other fix and flippers
Background: company is new so not any background
Market: is basically anyone selling a house or buying a house. Someone that needs to sell house fast. Basically I am a cash home buyer!!!

Email on card should be:   harborvalepropertiesinc@example-mail.com

Industry/Entity Type
House
Contact Information for Business Card
Harbor Vale Properties Inc
PO Box 718264
Coral Marsh FL 34197

Dale Morcott
dmorcott@example-mail.com
555-271-9083

```html
<!DOCTYPE html>
<html lang="en">
<head>
<meta charset="utf-8">
<title>Harbor Vale Properties Inc – Business Card</title>
<link rel="stylesheet" href="https://fonts.googleapis.com/css2?family=Arimo:wght@400;700&family=Roboto+Slab:wght@300;400&display=swap">
<style>
  :root {
    --bg: #d4d4d4;
    --card-black: #0c0c0c;
    --card-glow: #4a4a4a;
    --green: #2f7a23;
    --green-deep: #23651a;
    --lime: #9ec24a;
    --brand-green: #2a6a1e;
    --text-light: #e6e6e6;
    --text-muted: #bdbdbd;
    --divider: #9a9a9a;
  }
  * { box-sizing: border-box; margin: 0; padding: 0; }
  html, body { width: 1200px; height: 1200px; overflow: hidden; }
  body {
    background: var(--bg);
    position: relative;
    font-family: "Arimo", Arial, sans-serif;
  }

  .brand-lockup {
    position: absolute;
    left: 40px; top: 150px;
    display: flex; align-items: center; gap: 16px;
  }
  .brand-lockup .brand-dot {
    width: 34px; height: 34px; border-radius: 50%;
    background: var(--brand-green);
  }
  .brand-lockup .brand-name {
    font-weight: 700; font-size: 40px;
    color: var(--brand-green);
    letter-spacing: 0.5px;
  }

  .card {
    position: absolute;
    width: 720px; height: 410px;
    border-radius: 30px;
    overflow: hidden;
    background: radial-gradient(ellipse at 40% 45%, var(--card-glow) 0%, #1c1c1c 45%, var(--card-black) 80%);
    box-shadow: 0 12px 30px rgba(0,0,0,0.35);
  }
  .card .wave { position: absolute; inset: 0; width: 100%; height: 100%; }

  .card-front { left: 150px; top: 300px; }
  .card-back  { left: 440px; top: 750px; }

  .card-front .card-brand {
    position: absolute; left: 40px; top: 168px;
    width: 280px; text-align: center;
    font-weight: 700; font-size: 20px; color: var(--text-light);
  }
  .card-front .divider {
    position: absolute; left: 340px; top: 60px;
    width: 2px; height: 210px;
    background: linear-gradient(to bottom, transparent, var(--divider), transparent);
  }
  .card-front .person { position: absolute; left: 370px; top: 38px; }
  .person .person-name {
    font-family: "Roboto Slab", Georgia, serif;
    font-weight: 400; font-size: 38px; letter-spacing: 1.5px;
    color: var(--text-light); text-transform: uppercase;
    white-space: nowrap;
  }
  .person .person-title {
    font-family: "Roboto Slab", Georgia, serif;
    font-size: 16px; color: var(--text-muted);
    margin-left: 60px;
  }
  .contact-list {
    position: absolute; left: 362px; top: 124px;
    list-style: none;
    display: flex; flex-direction: column; gap: 11px;
  }
  .contact-list li {
    display: flex; align-items: center; gap: 12px;
    font-size: 19px; color: var(--text-light);
    white-space: nowrap;
  }
  .contact-list .icon {
    width: 28px; height: 28px; border-radius: 7px;
    background: var(--green); flex: none;
    display: flex; align-items: center; justify-content: center;
  }
  .contact-list .icon svg { width: 18px; height: 18px; }

  .card-back .card-brand {
    position: absolute; left: 0; width: 560px; top: 150px;
    text-align: center;
    font-weight: 700; font-size: 24px; color: var(--text-light);
  }
  .card-back .tagline {
    position: absolute; left: 0; width: 560px; top: 258px;
    text-align: center;
    font-family: "Roboto Slab", Georgia, serif;
    font-size: 32px; letter-spacing: 1.5px; color: var(--text-light);
  }
  .card-back .tagline-rule {
    position: absolute; left: 125px; top: 304px;
    width: 310px; height: 4px;
    background: linear-gradient(to right, transparent, var(--green) 20%, var(--green) 80%, transparent);
  }
</style>
</head>
<body>

  <div class="brand-lockup">
    <span class="brand-dot"></span>
    <span class="brand-name">Harbor Vale Properties Inc</span>
  </div>

  <section class="card card-front" aria-label="Business card front">
    <svg class="wave" viewBox="0 0 720 410" preserveAspectRatio="none" aria-hidden="true">
      <path d="M0 335 C 260 335, 590 320, 720 245 L720 410 L0 410 Z" fill="var(--green)"/>
      <path d="M0 335 C 260 335, 590 320, 720 245" fill="none" stroke="var(--lime)" stroke-width="5"/>
    </svg>
    <div class="card-brand">Harbor Vale Properties Inc</div>
    <div class="divider"></div>
    <div class="person">
      <div class="person-name">Dale Morcott</div>
      <div class="person-title">Managing Director</div>
    </div>
    <ul class="contact-list">
      <li><span class="icon"><svg viewBox="0 0 24 24" fill="#fff"><path d="M6.6 10.8a15 15 0 0 0 6.6 6.6l2.2-2.2c.3-.3.7-.4 1-.2 1.1.4 2.3.6 3.6.6.6 0 1 .4 1 1V20c0 .6-.4 1-1 1A17 17 0 0 1 3 4c0-.6.4-1 1-1h3.5c.6 0 1 .4 1 1 0 1.3.2 2.5.6 3.6.1.3 0 .7-.2 1z"/></svg></span>555-271-9083</li>
      <li><span class="icon"><svg viewBox="0 0 24 24" fill="#fff"><path d="M3 5h18v14H3z"/><path d="M3 5l9 7 9-7" fill="none" stroke="#2f7a23" stroke-width="2"/></svg></span>dmorcott@example-mail.com</li>
      <li><span class="icon"><svg viewBox="0 0 24 24" fill="#fff"><path d="M4 8h16v11H4z"/><path d="M4 8l4-4h8l4 4" fill="none" stroke="#fff" stroke-width="2"/></svg></span>PO Box 718264</li>
      <li><span class="icon"><svg viewBox="0 0 24 24" fill="#fff"><path d="M12 3l9 8h-3v9h-4v-6h-4v6H6v-9H3z"/></svg></span>Coral Marsh FL 34197</li>
    </ul>
  </section>

  <section class="card card-back" aria-label="Business card back">
    <svg class="wave" viewBox="0 0 720 410" preserveAspectRatio="none" aria-hidden="true">
      <path d="M540 0 C 640 90, 660 260, 600 410 L720 410 L720 0 Z" fill="var(--green-deep)"/>
      <path d="M540 0 C 640 90, 660 260, 600 410" fill="none" stroke="var(--lime)" stroke-width="4"/>
    </svg>
    <div class="card-brand">Harbor Vale Properties Inc</div>
    <div class="tagline">BUY HOUSES CASH</div>
    <div class="tagline-rule"></div>
  </section>

</body>
</html>
```